Pebblestone Promotions Flyer Design

I need to be able to have a flyer that shows what I do for businesses. Same logo that you designed.

Requirements
Must have
• I gave an example of what I need it to say in the attachment. Must have logo and resemble business card style.
Nice to have
• It could include pictures of what a digital sign is. We offer an KVRT, weather, and news slide on our advertising. I included sample pictures of those.

```html
<!DOCTYPE html>
<html lang="en">
<head>
<meta charset="utf-8">
<title>Pebblestone Promotions Flyer</title>
<link rel="stylesheet" href="https://fonts.googleapis.com/css2?family=Open+Sans:wght@400;600;700&display=swap">
<style>
:root{
  --green:#8cc63f;
  --ink:#1d1d1d;
  --grey:#5a5a5a;
  --frame:#2b2d31;
  --footer:#141414;
  --page:#e9e7e4;
  --white:#ffffff;
}
*{box-sizing:border-box;margin:0;padding:0}
html,body{width:1057px;height:1200px;overflow:hidden;background:var(--page);font-family:'Open Sans',Arial,sans-serif;color:var(--ink)}
.flyer{position:absolute;left:80px;top:16px;width:786px;height:1024px;background:var(--white);transform:scale(1.14);transform-origin:top left;box-shadow:0 4px 14px rgba(0,0,0,.25);overflow:hidden}
.hero{position:absolute;left:0;top:0;width:786px;height:355px;background:var(--frame)}
.hero-photo{position:absolute;left:45px;top:22px;width:712px;height:311px;background:linear-gradient(90deg,#3b4a66 0%,#56607a 35%,#8a93a6 50%,#f3f3f3 68%,#ffffff 100%)}
.brand-panel{position:absolute;left:395px;top:0;width:391px;height:98px;background:var(--white);clip-path:polygon(0 0,100% 0,100% 100%,11% 100%);box-shadow:0 2px 6px rgba(0,0,0,.3)}
.brand-name{position:absolute;right:22px;top:32px;font-size:27px;font-weight:600;color:var(--grey);letter-spacing:-.3px}
.what-we-do{position:absolute;left:417px;top:120px;width:326px;text-align:right}
.what-we-do h2{font-size:17px;font-weight:700;color:var(--green);margin-bottom:8px}
.what-we-do p{font-size:12.5px;line-height:17px;text-align:justify;text-align-last:right;margin-bottom:16px}
.benefits{position:absolute;left:0;top:355px;width:786px;height:285px;background:var(--green);color:var(--white)}
.benefits h2{position:absolute;left:26px;top:20px;font-size:17px;font-weight:600;letter-spacing:-.2px}
.benefit-list{position:absolute;left:26px;top:55px;width:512px;list-style:none}
.benefit-list li{position:relative;padding-left:22px;font-size:12.3px;line-height:16.8px;margin-bottom:8px;text-align:justify}
.benefit-list svg{position:absolute;left:0;top:1px}
.screen{position:absolute;left:561px;width:205px;background:var(--frame);padding:7px}
.screen div{width:100%;height:100%}
.screen-weather{top:23px;height:122px}
.screen-weather div{background:linear-gradient(160deg,#3f5fb0,#2c4592)}
.screen-sports{top:163px;height:110px}
.screen-sports div{background:linear-gradient(90deg,#2c2a28 0%,#5a4a40 30%,#c9c6c4 55%,#7d5a4c 100%)}
.process h2{position:absolute;left:26px;top:652px;font-size:17px;font-weight:600}
.step{position:absolute}
.pill{display:block;height:30px;line-height:30px;padding-left:28px;font-size:17px;font-weight:600;color:var(--white);background:var(--green);border-radius:0 14px 14px 0;margin-bottom:6px}
.step p{padding-left:26px;font-size:14px;line-height:17px;text-align:justify}
.step small{display:block;padding-left:26px;font-size:11px;line-height:15px;margin-top:4px}
.step-day1{left:0;top:681px;width:380px}
.step-day1 .pill{width:188px}
.step-day1 p{text-align:left;white-space:nowrap}
.step-week1{left:0;top:746px;width:380px}
.step-week1 .pill{width:188px}
.step-weeks{left:392px;top:681px;width:380px}
.step-weeks .pill{width:188px}
.step-weeks p,.step-weeks small,.step-end p{padding-left:28px}
.step-end{left:392px;top:780px;width:380px}
.step-end .pill{width:240px}
.step-end strong{display:block;padding-left:30px;font-size:14.5px;line-height:19px;font-weight:700;margin-top:22px}
.pay-line{position:absolute;left:26px;top:930px;font-size:16px}
.footer{position:absolute;left:0;top:990px;width:786px;height:34px;background:var(--footer);color:var(--white);font-size:12px}
.footer .email{position:absolute;left:22px;top:9px}
.footer .url{position:absolute;right:20px;top:9px}
.phone-tab{position:absolute;left:236px;top:982px;width:316px;height:42px;background:var(--green);clip-path:polygon(3% 0,97% 0,100% 100%,0 100%);color:var(--white);font-size:19px;display:flex;align-items:center;justify-content:center;gap:10px}
</style>
</head>
<body>
<main class="flyer">
  <section class="hero">
    <div class="hero-photo" role="img" aria-label="Worker clearing fallen snowy branches in front of a house at dusk"></div>
    <div class="brand-panel"><span class="brand-name">Pebblestone Promotions</span></div>
    <div class="what-we-do">
      <h2>WHAT WE DO:</h2>
      <p>We provide monthly payments to businesses for allowing us to advertise local businesses on a TV screen in your place of business.</p>
      <p>We provide the TV screen if you prefer (professional installation on our dime)</p>
      <p>We provide a win/win for the businesses that partner with us. Our business partners get paid to support local businesses.</p>
    </div>
  </section>

  <section class="benefits">
    <h2>BENEFITS OF PARTNERING WITH PEBBLESTONE PROMOTIONS</h2>
    <ul class="benefit-list">
      <li><svg width="15" height="14" viewBox="0 0 15 14"><rect x="1" y="2" width="11" height="11" rx="2" fill="none" stroke="#fff" stroke-width="1.5"/><path d="M3.5 7l3 3L14 1.5" fill="none" stroke="#fff" stroke-width="2"/></svg>WE PAY YOU!</li>
      <li><svg width="15" height="14" viewBox="0 0 15 14"><rect x="1" y="2" width="11" height="11" rx="2" fill="none" stroke="#fff" stroke-width="1.5"/><path d="M3.5 7l3 3L14 1.5" fill="none" stroke="#fff" stroke-width="2"/></svg>We advertise local businesses and business owners. We encourage them to stop by your establishment to check out their ad. This will create more foot traffic to your business.</li>
      <li><svg width="15" height="14" viewBox="0 0 15 14"><rect x="1" y="2" width="11" height="11" rx="2" fill="none" stroke="#fff" stroke-width="1.5"/><path d="M3.5 7l3 3L14 1.5" fill="none" stroke="#fff" stroke-width="2"/></svg>Waiting Rooms: Studies show perceived wait time can be decreased by up to 33% when there is digital signage present. This can make your clients’ 60 min wait feel like a 40 min wait.</li>
      <li><svg width="15" height="14" viewBox="0 0 15 14"><rect x="1" y="2" width="11" height="11" rx="2" fill="none" stroke="#fff" stroke-width="1.5"/><path d="M3.5 7l3 3L14 1.5" fill="none" stroke="#fff" stroke-width="2"/></svg>Professional ticker at the bottom of the digital design can display sports updates, breaking news, and weather. Our design approach makes your business look more professional.</li>
      <li><svg width="15" height="14" viewBox="0 0 15 14"><rect x="1" y="2" width="11" height="11" rx="2" fill="none" stroke="#fff" stroke-width="1.5"/><path d="M3.5 7l3 3L14 1.5" fill="none" stroke="#fff" stroke-width="2"/></svg>Did we mention that we pay you?!!!</li>
    </ul>
    <div class="screen screen-weather"><div role="img" aria-label="Digital sign showing a weather forecast slide"></div></div>
    <div class="screen screen-sports"><div role="img" aria-label="Viewer watching a KVRT sports news slide on a wall screen"></div></div>
  </section>

  <section class="process">
    <h2>EFFORTLESS PROCESS</h2>
    <div class="step step-day1">
      <span class="pill">Day 1:</span>
      <p>Sign on to partner with Pebblestone Promotions.</p>
    </div>
    <div class="step step-week1">
      <span class="pill">Week 1:</span>
      <p>We install a HDMI/USB drive to the screen. Our onsite time for this is less than 10 minutes and this WILL NOT disrupt your business operations. In fact, you may not even notice we came and went.</p>
      <small>(We can use an existing screen or install a new screen at no cost to you if space permits)</small>
    </div>
    <div class="step step-weeks">
      <span class="pill">Week 1-8:</span>
      <p>We will be loading our local advertisers’ professional designs to the screen.</p>
      <small>(This is done remotely and does not require us to come in)</small>
    </div>
    <div class="step step-end">
      <span class="pill">End of 2nd Full Month:</span>
      <p>Process is complete, and you will be receiving monthly checks!</p>
      <strong>Notice your involvement is only in the first and last step. Sign-up. Get Paid.</strong>
    </div>
    <p class="pay-line">We will pay you _____________ each month. Call for details__________________________.</p>
  </section>

  <footer class="footer">
    <span class="email">hello@pebblestonepromo.com</span>
    <span class="url">www.pebblestonepromo.com</span>
  </footer>
  <div class="phone-tab">
    <svg width="20" height="20" viewBox="0 0 20 20"><circle cx="10" cy="10" r="8.5" fill="none" stroke="#fff" stroke-width="1.6"/><path d="M7 5.5l1.6 2.2-1 1.2c.7 1.5 1.8 2.6 3.3 3.3l1.2-1 2.2 1.6-.9 1.7c-3.8-.4-7-3.6-7.4-7.4z" fill="#fff"/></svg>
    <span>+123 555 01987</span>
  </div>
</main>
</body>
</html>
```